Caldmere Plant and Skip Hire Business Card

We need a business card designed for an existing business to leave behind and encourage users to leave a google review, with the business details on the reverse so they can also keep the card as a business card, but the main aim is to generate google reviews so this side should be bigger and brighter.

Target Market(s)

Customers / Homeowners/ Builders

Industry/Entity Type

Waste Management

Contact Information for Business Card

Business title should be as per picture of lorry (for reference only) in yellow with black border around with the company name as

Caldmere Plant and Skip Hire

Did we provide good service? We'd love it if you left a Google review here:

g.page/caldmereskiphire

With five yellow stars under this

On the reverse I would like the same title again in yellow with a black outline
and the address, phone number, and website address in a plain black font

Tallow Brook Farm, Wenning Vale,
Caldmere, Oxfordshire. OX19 8QT
01742 596381

www.caldmereplanthire.co.uk

Font styles to use
Sans Serif

Colors
ec1f27
fbed22

Requirements
Must have
• Five yellow stars like a google review
Nice to have
• Clean and clear

```html
<!DOCTYPE html>
<html lang="en">
<head>
<meta charset="utf-8">
<title>Caldmere Plant &amp; Skip Hire – Business Card</title>
<link rel="stylesheet" href="https://fonts.googleapis.com/css2?family=Lato:wght@700;900&family=Questrial&family=Jost:wght@600&display=swap">
<style>
  :root {
    --backdrop: #c3c3bb;
    --red-top: #c8454f;
    --red-bottom: #a01a28;
    --accent-red: #b01e2a;
    --yellow: #e9c02e;
    --card-white: #f3f3f3;
    --ink: #555555;
    --url-ink: #f1e6e6;
  }
  * { box-sizing: border-box; margin: 0; padding: 0; }
  html, body { width: 1200px; height: 1196px; overflow: hidden; }
  body { background: var(--backdrop); position: relative; }

  .card {
    position: absolute;
    left: 243px;
    width: 727px;
    height: 405px;
  }
  .card--front {
    top: 150px;
    background: linear-gradient(to bottom, var(--red-top), var(--red-bottom));
  }
  .card--back {
    top: 603px;
    background: var(--card-white);
  }

  .company-title {
    position: absolute;
    left: 0; right: 0;
    top: 178px;
    padding-left: 16px;
    text-align: center;
    font-family: "Lato", sans-serif;
    font-weight: 900;
    font-size: 42px;
    letter-spacing: -1px;
    color: var(--yellow);
    white-space: nowrap;
  }
  .review-link {
    position: absolute;
    left: 0; right: 0;
    top: 310px;
    text-align: center;
    font-family: "Questrial", sans-serif;
    font-size: 21px;
    color: var(--url-ink);
  }
  .review-stars {
    position: absolute;
    left: 270px;
    top: 347px;
    width: 180px;
    height: 26px;
  }

  .holder-name {
    position: absolute;
    left: 93px;
    top: 168px;
    font-family: "Jost", sans-serif;
    font-weight: 600;
    font-size: 31px;
    letter-spacing: 5px;
    color: var(--ink);
  }
  .contact-list {
    position: absolute;
    left: 93px;
    top: 236px;
    list-style: none;
    font-family: "Questrial", sans-serif;
    font-size: 17px;
    line-height: 20.5px;
    color: var(--ink);
  }
  .contact-item {
    position: relative;
    padding-left: 34px;
  }
  .contact-item--web { margin-top: 20px; }
  .contact-icon {
    position: absolute;
    left: 0;
    top: 3px;
    width: 16px;
    height: 16px;
  }
</style>
</head>
<body>

<section class="card card--front">
  <h1 class="company-title">CALDMERE PLANT &amp; SKIP HIRE</h1>
  <p class="review-link">g.page/caldmereskiphire</p>
  <svg class="review-stars" viewBox="0 0 180 26" role="img" aria-label="Five star rating">
    <defs>
      <polygon id="star" fill="#e6bd2c" points="13,0 16.1,8.8 25.4,9 18,14.7 20.7,23.7 13,18.4 5.3,23.7 8,14.7 0.6,9 9.9,8.8"/>
    </defs>
    <use href="#star" x="0"/>
    <use href="#star" x="38.5"/>
    <use href="#star" x="77"/>
    <use href="#star" x="115.5"/>
    <use href="#star" x="154"/>
  </svg>
</section>

<section class="card card--back">
  <h2 class="holder-name">YOUR NAME</h2>
  <ul class="contact-list">
    <li class="contact-item">
      <svg class="contact-icon" viewBox="0 0 16 16" aria-hidden="true">
        <path fill="var(--accent-red)" d="M8 1a5 5 0 0 0-5 5c0 3.6 5 9 5 9s5-5.4 5-9a5 5 0 0 0-5-5zm0 7a2 2 0 1 1 0-4 2 2 0 0 1 0 4z"/>
      </svg>
      Tallow Brook Farm, Wenning Vale,<br>Caldmere, Oxfordshire. OX19 8QT
    </li>
    <li class="contact-item">
      <svg class="contact-icon" viewBox="0 0 16 16" aria-hidden="true">
        <rect x="3.5" y="0.8" width="9" height="14.4" rx="1.2" fill="none" stroke="var(--accent-red)" stroke-width="1.2"/>
        <line x1="6.5" y1="13" x2="9.5" y2="13" stroke="var(--accent-red)" stroke-width="1"/>
      </svg>
      01742 596381
    </li>
    <li class="contact-item contact-item--web">
      <svg class="contact-icon" viewBox="0 0 16 16" aria-hidden="true">
        <g fill="none" stroke="var(--accent-red)" stroke-width="1">
          <circle cx="8" cy="8" r="6.5"/>
          <ellipse cx="8" cy="8" rx="3" ry="6.5"/>
          <line x1="1.5" y1="8" x2="14.5" y2="8"/>
          <line x1="2.5" y1="4.8" x2="13.5" y2="4.8"/>
          <line x1="2.5" y1="11.2" x2="13.5" y2="11.2"/>
        </g>
      </svg>
      www.caldmereplanthire.co.uk
    </li>
  </ul>
</section>

</body>
</html>
```